Tarvel Ridge LLC

Need Professional Business cards for New Investment Fund

Target Market(s)

High Quality investors

Industry/Entity Type

Financial

Contact Information for Business Card

Phone Number +1 555 284 6193
Name Pavel Orlinsky
Title Fund Manager
email po@FundTarvel.example
Website www.FundTarvel.example

Colors

Designer to choose colors to be used in the design.

Requirements
Must have
• Must have our Logo and all of the above. Must be made so lettering and loge can be raised

```html
<!DOCTYPE html>
<html lang="en">
<head>
<meta charset="UTF-8">
<title>Tarvel Ridge LLC – Business Card</title>
<link href="https://fonts.googleapis.com/css2?family=Montserrat:wght@400;500;600;700&display=swap" rel="stylesheet">
<style>
  :root {
    --backdrop: #2b2522;
    --card: #2e2e30;
    --card-deep: #262628;
    --pattern-light: #38383b;
    --edge-green: #3fe21c;
    --accent-green: #3fe21c;
    --ink-white: #f2f2f2;
    --rule: #d9d9d9;
  }
  * { margin: 0; padding: 0; box-sizing: border-box; }
  html, body {
    width: 1200px;
    height: 800px;
    overflow: hidden;
    background: var(--backdrop);
    font-family: "Montserrat", sans-serif;
  }
  .canvas {
    position: relative;
    width: 1200px;
    height: 800px;
  }
  .card {
    position: absolute;
    top: 252px;
    width: 520px;
    height: 297px;
    background: var(--card);
    border: 2px solid var(--edge-green);
    overflow: hidden;
  }
  /* Back side */
  .card-back { left: 50px; }
  .back-pattern {
    position: absolute;
    inset: 0;
    background: linear-gradient(135deg, var(--pattern-light) 0%, var(--card-deep) 55%, var(--pattern-light) 100%);
  }
  .back-mark {
    position: absolute;
    right: 26px;
    bottom: 24px;
    display: flex;
    align-items: center;
    gap: 8px;
    font-weight: 600;
    font-size: 13px;
    letter-spacing: 0.5px;
    color: var(--ink-white);
  }
  .mark-square {
    width: 12px;
    height: 12px;
    background: var(--accent-green);
  }
  /* Front side */
  .card-front { left: 630px; }
  .brand {
    position: absolute;
    left: 38px;
    top: 46px;
    display: flex;
    align-items: center;
    gap: 12px;
    font-weight: 600;
    font-size: 22px;
    letter-spacing: 0.5px;
    color: var(--ink-white);
  }
  .brand .mark-square { width: 20px; height: 20px; }
  .rule {
    position: absolute;
    height: 1px;
    background: var(--rule);
  }
  .rule-top { left: 38px; right: 0; top: 128px; }
  .rule-bottom { left: 250px; right: 24px; top: 262px; }
  .contact-list {
    position: absolute;
    left: 30px;
    top: 152px;
    list-style: none;
  }
  .contact-item {
    display: flex;
    align-items: center;
    gap: 9px;
    height: 22px;
    font-size: 13.5px;
    font-weight: 400;
    color: var(--ink-white);
  }
  .contact-item svg { width: 12px; height: 12px; flex: none; }
  .person {
    position: absolute;
    right: 30px;
    top: 212px;
    text-align: right;
  }
  .person-name {
    font-weight: 700;
    font-size: 17px;
    letter-spacing: 0.8px;
    text-transform: uppercase;
    color: var(--accent-green);
  }
  .person-title {
    font-size: 13.5px;
    font-weight: 400;
    color: var(--ink-white);
    margin-top: 1px;
  }
</style>
</head>
<body>
<main class="canvas">

  <section class="card card-back">
    <div class="back-pattern" role="img" aria-label="Repeating embossed brand monogram pattern in dark grey tones"></div>
    <div class="back-mark"><span class="mark-square"></span>Tarvel Ridge</div>
  </section>

  <section class="card card-front">
    <div class="brand"><span class="mark-square"></span>Tarvel Ridge</div>
    <div class="rule rule-top"></div>

    <ul class="contact-list">
      <li class="contact-item">
        <svg viewBox="0 0 24 24" fill="var(--accent-green)" aria-hidden="true"><path d="M6.6 10.8a15.1 15.1 0 0 0 6.6 6.6l2.2-2.2a1 1 0 0 1 1-.25 11.4 11.4 0 0 0 3.6.57 1 1 0 0 1 1 1V20a1 1 0 0 1-1 1A17 17 0 0 1 3 4a1 1 0 0 1 1-1h3.5a1 1 0 0 1 1 1c0 1.25.2 2.45.57 3.57a1 1 0 0 1-.25 1z"/></svg>
        +1 555 284 6193
      </li>
      <li class="contact-item">
        <svg viewBox="0 0 24 24" fill="var(--accent-green)" aria-hidden="true"><path d="M2 5h20v14H2z M3.5 6.5 12 13l8.5-6.5" stroke="var(--card)" stroke-width="1.6"/></svg>
        po@FundTarvel.example
      </li>
      <li class="contact-item">
        <svg viewBox="0 0 24 24" fill="none" stroke="var(--accent-green)" stroke-width="2.4" aria-hidden="true"><circle cx="12" cy="12" r="9.5"/><path d="M2.5 12h19M12 2.5c3 3 3 16 0 19M12 2.5c-3 3-3 16 0 19"/></svg>
        www.FundTarvel.example
      </li>
    </ul>

    <div class="person">
      <p class="person-name">Pavel Orlinsky</p>
      <p class="person-title">Fund Manager</p>
    </div>
    <div class="rule rule-bottom"></div>
  </section>

</main>
</body>
</html>
```